Bramblewick Gardening Services. A6 flyer single sided

Need an A6 flyer designing. Single sided.
I am a gardener.
I do lawn mowing - one-off garden tidy ups or regular fortnightly visits.
All kinds of trees expertly felled, topped or pruned.
Hedge cutting.
Fencing replaced or repaired.
Fully insured.
Access to fully qualified and licenced tree arborist
07724 316048 or 01632 742918.

I have attached my business card and letter head logo.
I'm open to new designs without incorporating any of my artwork.

Industry/Entity Type

Gardener

```html
<!DOCTYPE html>
<html lang="en">
<head>
<meta charset="utf-8">
<title>Bramblewick Garden Services – Flyer</title>
<link href="https://fonts.googleapis.com/css2?family=Bebas+Neue&family=Roboto+Condensed:wght@400;700&display=swap" rel="stylesheet">
<style>
  :root {
    --green-band: #1b733a;
    --green-deep: #1d4a2a;
    --green-head: #1d6b3b;
    --green-icon: #6c9b74;
    --grass-light: #9fc276;
    --grass-mid: #5f8f3e;
    --grass-deep: #2e5722;
    --white: #ffffff;
  }
  * { margin: 0; padding: 0; box-sizing: border-box; }
  html, body { width: 849px; height: 1200px; overflow: hidden; background: #ffffff; }
  .flyer {
    position: relative;
    width: 849px;
    height: 1200px;
    overflow: hidden;
    background: var(--green-band);
    font-family: "Bebas Neue", "Oswald", sans-serif;
  }
  .hero-photo {
    position: absolute;
    left: 0; top: 0;
    width: 849px; height: 800px;
    background:
      radial-gradient(circle at 660px 260px, #f2f6ec 0, #dbe9cf 50px, rgba(219,233,207,0) 120px),
      radial-gradient(circle at 40px 220px, #e4eedb 0, rgba(228,238,219,0) 110px),
      radial-gradient(ellipse at 300px 420px, #7aa25a 0, rgba(122,162,90,0) 320px),
      linear-gradient(180deg, var(--grass-light) 0%, var(--grass-mid) 45%, var(--grass-deep) 100%);
  }
  .headline {
    position: absolute;
    left: 0; top: 86px;
    width: 849px;
    text-align: center;
    font-size: 100px;
    font-weight: 400;
    line-height: 1;
    color: var(--green-head);
    white-space: nowrap;
  }
  .headline .accent { color: var(--white); }
  .service-band { position: absolute; left: 0; top: 0; width: 849px; height: 1200px; }
  .service-label {
    position: absolute;
    top: 852px;
    width: 220px;
    margin-left: -110px;
    text-align: center;
    font-size: 38px;
    line-height: 1;
    color: var(--white);
  }
  .brand {
    position: absolute;
    left: 36px; top: 958px;
    width: 392px;
  }
  .brand-name {
    font-size: 82px;
    line-height: 0.86;
    color: var(--green-deep);
    white-space: nowrap;
  }
  .brand-tag {
    font-size: 68px;
    line-height: 0.95;
    color: var(--white);
    white-space: nowrap;
  }
  .phones {
    margin-top: 8px;
    text-align: right;
    padding-right: 12px;
    font-size: 44px;
    line-height: 0.9;
    color: var(--green-deep);
  }
  .divider {
    position: absolute;
    left: 453px; top: 960px;
    width: 4px; height: 200px;
    background: var(--green-deep);
  }
  .about {
    position: absolute;
    left: 476px; top: 960px;
    width: 340px;
    color: var(--white);
    font-family: "Roboto Condensed", "Arial Narrow", sans-serif;
    text-transform: uppercase;
  }
  .about-title { font-size: 19px; font-weight: 700; line-height: 1.2; margin-bottom: 2px; }
  .about-body { font-size: 14px; font-weight: 400; line-height: 1.33; }
</style>
</head>
<body>
<main class="flyer">
  <div class="hero-photo" role="img" aria-label="Close-up photograph of a garden ornament standing in tall green grass"></div>

  <h1 class="headline">When <span class="accent">Quality</span> Matters!</h1>

  <svg class="service-band" width="849" height="1200" viewBox="0 0 849 1200" aria-hidden="true">
    <rect x="0" y="789" width="849" height="411" fill="var(--green-band)"/>
    <g fill="var(--green-band)" stroke="#2a8a48" stroke-width="2">
      <circle cx="140" cy="791" r="60"/>
      <circle cx="328" cy="791" r="60"/>
      <circle cx="517" cy="791" r="60"/>
      <circle cx="705" cy="791" r="60"/>
    </g>
    <rect x="0" y="790" width="849" height="60" fill="var(--green-band)"/>
    <g fill="var(--green-icon)">
      <circle cx="140" cy="791" r="47"/>
      <circle cx="328" cy="791" r="47"/>
      <circle cx="517" cy="791" r="47"/>
      <circle cx="705" cy="791" r="47"/>
    </g>
    <g fill="none" stroke="var(--white)" stroke-width="2.5" stroke-linecap="round" stroke-linejoin="round">
      <g class="icon-shears">
        <path d="M126 764 L146 792 M154 764 L134 792"/>
        <path d="M134 792 q-10 10 -6 22 q8 4 14 -8 z"/>
        <path d="M146 792 q10 10 6 22 q-8 4 -14 -8 z"/>
      </g>
      <g class="icon-mower">
        <path d="M306 766 L324 798"/>
        <path d="M318 798 h30 l4 12 h-38 z"/>
        <circle cx="322" cy="814" r="5"/>
        <circle cx="346" cy="814" r="5"/>
      </g>
      <g class="icon-fence">
        <path d="M497 812 v-32 l5 -7 l5 7 v32 M510 812 v-36 l5 -7 l5 7 v36 M523 812 v-32 l5 -7 l5 7 v32"/>
        <path d="M494 786 h42 M494 802 h42"/>
      </g>
      <g class="icon-tree">
        <circle cx="705" cy="782" r="18"/>
        <path d="M705 800 v16 M695 816 h20 M705 790 l-7 -7 M705 794 l8 -8"/>
      </g>
    </g>
  </svg>

  <div class="service-label" style="left:140px">Visits</div>
  <div class="service-label" style="left:328px">Lawn Mowing</div>
  <div class="service-label" style="left:517px">Fencing</div>
  <div class="service-label" style="left:705px">Tree Work</div>

  <section class="brand">
    <div class="brand-name">Bramblewick</div>
    <div class="brand-tag">Garden Services</div>
    <div class="phones">
      <div class="phone">01632 742 918</div>
      <div class="phone">07724 316 048</div>
    </div>
  </section>

  <div class="divider"></div>

  <section class="about">
    <h2 class="about-title">Fully insured gardener</h2>
    <p class="about-body">One-off garden tidy ups or regular fortnightly visits. Lawn mowing and hedge cutting, plus all kinds of trees expertly felled, topped or pruned. Fencing replaced or repaired. Access to a fully qualified and licenced tree arborist for larger jobs. Call 07724 316048 or 01632 742918 today to book your visit.</p>
  </section>
</main>
</body>
</html>
```